Bramwell Resources Ltd. - Refreshed business card challenge

A revised, refreshed business card design for my oil and gas company using my existing logo. Feel free to be as creative as you like!

Target Market(s)

bankers, lawyers

Industry/Entity Type

Oil And Gas Exploration

Contact Information for Business Card

See the "Must Haves" section

Font styles to use
Serif
Sans Serif

Colors

Designer to choose colors to be used in the design.

Requirements
Must have
• Existing business logo, name, title, email, phone number, business address
• Neil Hadley, CA, CPA
• Vice President Finance & Chief Financial Officer
• nhadley@bramwellresources-mail.com
• office: (587)555-0142
• cell: (403)555-0187
• 1400, 815 4 Street S.W.
• Calgary, AB
• T2P 4K8
Should not have
• Should not be plain and boring.

```html
<!DOCTYPE html>
<html lang="en">
<head>
<meta charset="UTF-8">
<title>Bramwell Resources Ltd. – Business Card</title>
<link href="https://fonts.googleapis.com/css2?family=Poppins:wght@400;500;600;700&display=swap" rel="stylesheet">
<style>
  :root {
    --forest: #1f5e45;
    --earth: #5a3620;
    --charcoal: #48484b;
    --charcoal-deep: #3a3a3d;
    --ink: #2b2b2b;
    --paper: #ffffff;
    --backdrop: #e9e6e1;
  }
  * { box-sizing: border-box; margin: 0; padding: 0; }
  html, body {
    width: 1200px; height: 960px; overflow: hidden;
    background: var(--backdrop);
    font-family: "Poppins", sans-serif;
  }
  .sheet {
    width: 1200px; height: 960px;
    display: flex; flex-direction: column; align-items: center;
    justify-content: center; gap: 32px;
  }
  .card {
    position: relative; width: 760px; height: 434px;
    border-radius: 4px; overflow: hidden;
    box-shadow: 0 8px 24px rgba(0,0,0,0.18);
  }

  /* Back side */
  .card--back {
    background: linear-gradient(100deg, var(--charcoal-deep) 0%, var(--charcoal) 55%, #5a5a5e 100%);
  }
  .back-brand {
    position: absolute; left: 70px; top: 170px;
    display: flex; align-items: center; gap: 16px;
  }
  .brand-mark { width: 26px; height: 26px; background: var(--forest); }
  .back-brand .brand-name {
    font-weight: 700; font-size: 44px; color: var(--forest); line-height: 1;
  }
  .back-email {
    position: absolute; right: 40px; bottom: 34px;
    color: var(--paper); font-size: 17px; font-weight: 500;
  }

  /* Front side */
  .card--front { background: var(--paper); }
  .front-brand {
    position: absolute; right: 44px; top: 58px;
    display: flex; align-items: center; gap: 10px;
  }
  .front-brand .brand-mark { width: 18px; height: 18px; }
  .front-brand .brand-name {
    font-weight: 700; font-size: 26px; color: var(--forest); line-height: 1;
  }
  .holder { position: absolute; left: 230px; top: 150px; }
  .holder-name { font-weight: 700; font-size: 32px; color: var(--forest); line-height: 1.1; }
  .holder-title { font-weight: 500; font-size: 12px; color: var(--earth); margin-top: 4px; }
  .details {
    position: absolute; left: 150px; top: 250px;
    display: flex; gap: 26px; color: var(--ink);
  }
  .address { font-size: 17px; font-weight: 500; line-height: 1.45; padding-top: 2px; }
  .divider { width: 2px; height: 86px; background: var(--forest); }
  .contact { font-size: 17px; font-weight: 500; line-height: 1.5; }
  .band { position: absolute; left: 0; bottom: 0; width: 760px; height: 40px; }
</style>
</head>
<body>
<main class="sheet">
  <section class="card card--back" aria-label="Card back">
    <div class="back-brand">
      <span class="brand-mark"></span>
      <span class="brand-name">Bramwell Resources</span>
    </div>
    <p class="back-email">nhadley@bramwellresources-mail.com</p>
  </section>

  <section class="card card--front" aria-label="Card front">
    <div class="front-brand">
      <span class="brand-mark"></span>
      <span class="brand-name">Bramwell Resources</span>
    </div>
    <div class="holder">
      <h1 class="holder-name">Neil Hadley, CA, CPA</h1>
      <p class="holder-title">Vice President Finance &amp; Chief Financial Officer</p>
    </div>
    <div class="details">
      <p class="address">1400, 815 4 Street S.W.<br>Calgary, AB, T2P 4K8</p>
      <span class="divider"></span>
      <p class="contact">Cell: 403-555-0187<br>office: (587)555-0142<br>nhadley@bramwellresources-mail.com</p>
    </div>
    <svg class="band" viewBox="0 0 760 40" preserveAspectRatio="none" aria-hidden="true">
      <polygon points="0,12 560,26 540,40 0,40" fill="#1f5e45"/>
      <polygon points="560,26 760,31 760,40 540,40" fill="#5a3620"/>
      <polygon points="0,40 760,40 760,36 0,30" fill="#ffffff" opacity="0"/>
    </svg>
  </section>
</main>
</body>
</html>
```